TOPページのイメージを作成していただきたいです。
女性が入りやすく、親しみやすい色使いとフォントで、
カテゴリのボタンはアイコン等を使い、やわらかい印象を与えたい
※アイコンを指定しているわけではありません。

商品にカラフルなものが多くなりやすいので、全体的な色バランスはシンプルなカラーでお願いします。
サイドバナーとメインに上記スクールをターゲットとしたカテゴリに飛ぶためのバナー用意してほしいです。
近いサイトイメージは合わせて送らせていただきます。
スマートフォンでも表示させやすいレイアウトを希望します。
Quelvoのショッピングに関しては、Quelvoプリズマを契約予定です。
また、今回はトップページだけですが、契約させて頂いた方には商品ページなどサブページも依頼する可能性が高いです

-------------------
項目について
-------------------
※スプレッドシート参照
https://sheets.tavrolink.com/spreadsheets/d/7pxQwLzNc4bTr2VhYk9MeJsA8uDfGiHo3nKyRtE5WqPl/edit?usp=sharing
■ヘッダー
検索窓、お支払いについて、送料、お届けについて、返品、交換、保証について、会社概要、プライバシーポリシー、お問い合わせ、よくある質問
■フッター
店舗内簡易情報として、イメージ画像のような下記の内容を用意する予定で、記述箇所のデザインを用意してください
送料について、支払い方法について、手数料、納期、キャンセルについて、商品の在庫について
■カテゴリ
カテゴリは、別紙の資料の通りです。
大カテゴリがメイン、中に小カテゴリがあります。

■写真資料
https://files.tavrolink.com/file/d/9kd3RwQ7mZ2xVbN8pLcT4yHsJfGeAu6Wn/view?usp=sharing

■サイト見本イメージ
https://store.mirubeta.jp/pastelnook/
https://yarn-lumio.com/
https://ec.stitchvale.jp/
https://www.tomiseki.co.jp/shop/c/c10/
https://www.webshop.mirel-kasano.com/
https://works.brevok.net/
サイトの色合いや雰囲気に近いサイトになります。
1ページ
赤系、黄・オレンジ系、茶系
• イラストレーター形式 (.ai)
幅1250px程度
※Quelvoショップのバナーサイズを考慮しています。
場合によってはその他のページもお願いする可能性があります。
もう少し提案数を頂きたいため、5月13日(金)までコンペの延長をいたします。

今回選ばせていただきました理由は
・商品を邪魔しないシンプルさ
・Quelvoショップに落とし込んだ時に差異が生まれにくい点
・全体的な色使い
を中心に選ばせていただきました。
非常にあたたかく、親しみやすいデザインで作成いただきましたので、こちらに決定させていただきました。

今回いただきました提案はどれも素晴らしく、選考は非常に悩みました。
冒険するか、無難なデザインにするか、また、その中でもどれがいいか、かなり悩みまして、選ばれなかったデザインも、最後までの残ったデザインがいくつかございました。
本当に皆様ご提案ありがとうございました。
また次の機会がございましたら、是非よろしくお願いします。

```html
<!DOCTYPE html>
<html lang="ja">
<head>
<meta charset="utf-8">
<title>ハンドメイド shop ぽるみ</title>
<link href="https://fonts.googleapis.com/css2?family=M+PLUS+Rounded+1c:wght@400;700;800&display=swap" rel="stylesheet">
<style>
:root{
  --bg:#e3cfb0;
  --brown:#8a4a2c;
  --panel:#f3f1ee;
  --white:#ffffff;
  --text:#5a3a28;
  --muted:#9a8878;
  --line:#d8d2cc;
  --cork:#b8895a;
  --tag:#d9342b;
}
*{box-sizing:border-box;margin:0;padding:0}
html,body{width:1200px;height:3584px;overflow:hidden}
body{background:var(--bg);font-family:"M PLUS Rounded 1c",sans-serif;color:var(--text);position:relative}
.abs{position:absolute}
.site-header{left:72px;top:72px;width:1048px;height:64px;background:var(--brown);display:flex;align-items:center;padding-left:16px}
.site-title{color:var(--white);font-size:28px;font-weight:700;letter-spacing:1px}
.search{position:absolute;left:604px;top:14px;width:352px;height:36px;background:var(--white);border-radius:18px}
.search svg{position:absolute;left:10px;top:8px}
.menu-btn{position:absolute;right:0;top:0;width:64px;height:64px;background:#c9b497;display:flex;align-items:center;justify-content:center}
.main-banner{left:208px;top:184px;width:808px;height:436px;background:var(--cork);padding:18px}
.main-banner .board{width:100%;height:100%;position:relative;border-radius:4px}
.main-banner .photos{position:absolute;inset:0;background:linear-gradient(135deg,#e9d6b6 0%,#cfae84 50%,#7c8c9e 100%);border-radius:4px}
.banner-copy{position:absolute;left:22px;top:40px;background:var(--white);padding:12px 20px;font-size:36px;font-weight:800;line-height:1.3;color:#2a2a2a;border-radius:4px}
.banner-copy em{font-style:normal;color:#c0392b}
.banner-more{position:absolute;right:22px;bottom:20px;background:var(--white);padding:8px 22px;font-size:18px;font-weight:700;border-radius:4px}
.section-tab{height:56px;width:288px;background:var(--panel);border-radius:28px 28px 0 0;display:flex;align-items:center;justify-content:center;font-size:30px;font-weight:800;color:var(--brown)}
.panel{background:var(--panel);border-radius:24px}
.card{position:absolute;width:216px}
.ph{display:block;position:relative}
.ph .tag{position:absolute;width:34px;height:16px;background:var(--tag)}
.card-name{font-size:28px;font-weight:700;text-align:center;color:#333}
.card-price{font-size:16px;text-align:center;color:var(--muted);margin-top:4px}
.more-btn{width:296px;height:48px;background:var(--panel);border-radius:24px;display:flex;align-items:center;justify-content:center;font-size:20px;font-weight:700;color:var(--brown)}
.grid{display:grid;grid-template-columns:repeat(4,168px);column-gap:40px;row-gap:48px}
.grid .ph{height:168px}
.grid .card-name{font-size:20px;margin-top:8px}
.grid .card-price{font-size:13px;margin-top:0}
.sidebar{left:912px;top:688px;width:208px;height:1792px;background:var(--panel)}
.side-banner{position:absolute;left:0;top:0;width:208px;height:216px;background:var(--cork);padding:8px}
.side-banner .inner{width:100%;height:100%;background:linear-gradient(160deg,#f2e6d0,#b8a58c);position:relative}
.side-banner .copy{position:absolute;left:6px;top:6px;background:var(--white);font-size:17px;font-weight:800;line-height:1.2;padding:4px 6px;color:#2a2a2a}
.side-banner .copy em{font-style:normal;color:#c0392b}
.side-banner .copy small{display:block;font-size:10px;font-weight:700}
.side-banner .go{position:absolute;right:6px;bottom:6px;background:var(--white);font-size:10px;padding:2px 6px}
.cat-title{position:absolute;left:8px;top:232px;font-size:32px;font-weight:800;color:var(--brown)}
.cat-list{position:absolute;left:8px;top:296px;width:184px;list-style:none}
.cat-list li{height:44px;border-bottom:1px solid var(--line);display:flex;align-items:center;justify-content:space-between;font-size:13px;color:#444;padding:0 4px}
.cat-list li.sub{padding-left:24px;border-bottom:none;height:32px}
.site-footer{left:0;top:3152px;width:1200px;height:368px;background:var(--brown)}
.footer-name{position:absolute;left:100px;top:172px;color:var(--white);font-size:22px;font-weight:700}
.footer-links{position:absolute;left:832px;top:120px;list-style:none;border-left:1px solid #c89a7e;padding-left:8px}
.footer-links li{color:#f1ddd0;font-size:22px;line-height:32px}
</style>
</head>
<body>

<header class="abs site-header">
  <span class="site-title">ハンドメイド shop ぽるみ</span>
  <div class="search">
    <svg width="20" height="20" viewBox="0 0 20 20"><circle cx="8" cy="8" r="6" fill="none" stroke="#333" stroke-width="2.5"/><line x1="12.5" y1="12.5" x2="18" y2="18" stroke="#333" stroke-width="2.5"/></svg>
  </div>
  <div class="menu-btn">
    <svg width="32" height="24" viewBox="0 0 32 24"><g stroke="#fff" stroke-width="3"><line x1="2" y1="3" x2="30" y2="3"/><line x1="2" y1="12" x2="30" y2="12"/><line x1="2" y1="21" x2="30" y2="21"/></g></svg>
  </div>
</header>

<section class="abs main-banner">
  <div class="board">
    <div class="photos" role="img" aria-label="イベント向け商品（プリント道具・Tシャツ・雑貨）の写真コラージュ"></div>
    <p class="banner-copy"><em>イベント向け</em>のアイテムも<br>各種取り揃えております!</p>
    <span class="banner-more">詳しくはこちら</span>
  </div>
</section>

<aside class="abs sidebar">
  <div class="side-banner">
    <div class="inner" role="img" aria-label="イベント向け商品の写真バナー">
      <p class="copy"><em>イベント向け</em><small>のアイテムも</small>各種取り揃えております!</p>
      <span class="go">詳しくはこちら</span>
    </div>
  </div>
  <h2 class="cat-title">カテゴリー</h2>
  <ul class="cat-list">
    <li>送料商品<svg width="8" height="12"><path d="M1 1l5 5-5 5" stroke="#666" fill="none" stroke-width="1.5"/></svg></li>
    <li>染色・ペイント・プリント<svg width="8" height="12"><path d="M1 1l5 5-5 5" stroke="#666" fill="none" stroke-width="1.5"/></svg></li>
    <li>加工素材<svg width="8" height="12"><path d="M1 1l5 5-5 5" stroke="#666" fill="none" stroke-width="1.5"/></svg></li>
    <li>梱包素材<svg width="8" height="12"><path d="M1 1l5 5-5 5" stroke="#666" fill="none" stroke-width="1.5"/></svg></li>
    <li>加工道具<svg width="8" height="12"><path d="M1 1l5 5-5 5" stroke="#666" fill="none" stroke-width="1.5"/></svg></li>
    <li>カット道具<svg width="8" height="12"><path d="M1 1l5 5-5 5" stroke="#666" fill="none" stroke-width="1.5"/></svg></li>
    <li>袋・箱<svg width="8" height="12"><path d="M1 1l5 5-5 5" stroke="#666" fill="none" stroke-width="1.5"/></svg></li>
    <li>雑貨<svg width="8" height="12"><path d="M1 1l5 5-5 5" stroke="#666" fill="none" stroke-width="1.5"/></svg></li>
    <li>アクセ作成<svg width="8" height="12"><path d="M1 1l5 5-5 5" stroke="#666" fill="none" stroke-width="1.5"/></svg></li>
    <li>バッグ作成<svg width="8" height="12"><path d="M1 1l5 5-5 5" stroke="#666" fill="none" stroke-width="1.5"/></svg></li>
    <li>アイロンシート作成<svg width="8" height="12"><path d="M1 1l5 5-5 5" stroke="#666" fill="none" stroke-width="1.5"/></svg></li>
    <li>セット商品</li>
    <li class="sub">イベントキット<svg width="8" height="12"><path d="M1 1l5 5-5 5" stroke="#666" fill="none" stroke-width="1.5"/></svg></li>
    <li class="sub">スタートキット<svg width="8" height="12"><path d="M1 1l5 5-5 5" stroke="#666" fill="none" stroke-width="1.5"/></svg></li>
  </ul>
</aside>

<h2 class="abs section-tab" style="left:344px;top:704px">おすすめ</h2>
<section class="abs panel recommend" style="left:80px;top:760px;width:816px;height:488px">
  <div class="card" style="left:32px;top:100px">
    <div class="ph" role="img" aria-label="商品写真：モノクロ柄のプリント生地" style="height:230px;background:linear-gradient(135deg,#e8e8e8,#555 60%,#c33)"><span class="tag" style="right:6px;bottom:8px"></span></div>
    <p class="card-name" style="margin-top:22px">商品名</p><p class="card-price">価格</p>
  </div>
  <div class="card" style="left:300px;top:100px">
    <div class="ph" role="img" aria-label="商品写真：プリントトートバッグ" style="height:230px;background:linear-gradient(160deg,#f0f0f0,#b9b9b9)"><span class="tag" style="left:92px;bottom:8px"></span></div>
    <p class="card-name" style="margin-top:22px">商品名</p><p class="card-price">価格</p>
  </div>
  <div class="card" style="left:568px;top:100px">
    <div class="ph" role="img" aria-label="商品写真：ポップアート調のプリント" style="height:230px;background:linear-gradient(135deg,#3b6fb5,#e8c9a8 55%,#c33)"><span class="tag" style="right:6px;top:8px"></span></div>
    <p class="card-name" style="margin-top:22px">商品名</p><p class="card-price">価格</p>
  </div>
</section>
<div class="abs more-btn" style="left:348px;top:1280px">もっとみる</div>

<h2 class="abs section-tab" style="left:344px;top:1432px">アイテム一覧</h2>
<section class="abs panel items" style="left:80px;top:1488px;width:816px;height:1384px;padding:32px 0 0 20px">
  <div class="grid">
    <div><div class="ph" role="img" aria-label="商品写真：白い雑貨" style="background:linear-gradient(#f4f4f4,#cfcfcf)"></div><p class="card-name">商品名</p><p class="card-price">価格</p></div>
    <div><div class="ph" role="img" aria-label="商品写真：文字プリント" style="background:linear-gradient(135deg,#fff,#e06a5a 60%,#3a6fb0)"></div><p class="card-name">商品名</p><p class="card-price">価格</p></div>
    <div><div class="ph" role="img" aria-label="商品写真：キーホルダー" style="background:linear-gradient(#f2f2f2,#2b2b3a)"></div><p class="card-name">商品名</p><p class="card-price">価格</p></div>
    <div><div class="ph" role="img" aria-label="商品写真：トートバッグ" style="background:linear-gradient(#efe9e0,#6b4a30)"><span class="tag" style="right:6px;top:6px"></span></div><p class="card-name">商品名</p><p class="card-price">価格</p></div>

    <div><div class="ph" role="img" aria-label="商品写真：カラフルなプリント" style="background:linear-gradient(135deg,#e2417a,#f2c230)"><span class="tag" style="left:6px;bottom:6px"></span></div><p class="card-name">商品名</p><p class="card-price">価格</p></div>
    <div><div class="ph" role="img" aria-label="商品写真：黒Tシャツ" style="background:linear-gradient(#d9d2c8,#222)"><span class="tag" style="right:6px;top:6px"></span></div><p class="card-name">商品名</p><p class="card-price">価格</p></div>
    <div><div class="ph" role="img" aria-label="商品写真：赤いTシャツ" style="background:linear-gradient(#e6ddd4,#c0392b)"><span class="tag" style="left:6px;bottom:6px"></span></div><p class="card-name">商品名</p><p class="card-price">価格</p></div>
    <div><div class="ph" role="img" aria-label="商品写真：青いTシャツ" style="background:linear-gradient(#e3ded8,#3a8fd0)"><span class="tag" style="left:6px;bottom:6px"></span></div><p class="card-name">商品名</p><p class="card-price">価格</p></div>

    <div><div class="ph" role="img" aria-label="商品写真：グレーTシャツ" style="background:linear-gradient(#eee,#8a8a8a)"><span class="tag" style="left:6px;top:6px"></span></div><p class="card-name">商品名</p><p class="card-price">価格</p></div>
    <div><div class="ph" role="img" aria-label="商品写真：グリーンのバッグ" style="background:linear-gradient(#d8d0c4,#4f6b4a)"></div><p class="card-name">商品名</p><p class="card-price">価格</p></div>
    <div><div class="ph" role="img" aria-label="商品写真：ネイビーTシャツ" style="background:linear-gradient(#ddd,#2e3550)"></div><p class="card-name">商品名</p><p class="card-price">価格</p></div>
    <div><div class="ph" role="img" aria-label="商品写真：白Tシャツ" style="background:linear-gradient(#f7f7f7,#c8c8c8)"><span class="tag" style="right:6px;top:6px"></span></div><p class="card-name">商品名</p><p class="card-price">価格</p></div>

    <div><div class="ph" role="img" aria-label="商品写真：赤いショートパンツ" style="background:linear-gradient(#f2f2f2,#d22a2a)"></div><p class="card-name">商品名</p><p class="card-price">価格</p></div>
    <div><div class="ph" role="img" aria-label="商品写真：黄色のウェア" style="background:linear-gradient(#eee,#e8c53a)"></div><p class="card-name">商品名</p><p class="card-price">価格</p></div>
    <div><div class="ph" role="img" aria-label="商品写真：黒いパンツ" style="background:linear-gradient(#f2f2f2,#1e1e1e)"><span class="tag" style="right:6px;top:6px"></span></div><p class="card-name">商品名</p><p class="card-price">価格</p></div>
    <div><div class="ph" role="img" aria-label="商品写真：青いウェア" style="background:linear-gradient(#8fc3e8,#1f4f8a)"></div><p class="card-name">商品名</p><p class="card-price">価格</p></div>

    <div><div class="ph" role="img" aria-label="商品写真：デニム調ウェア" style="background:linear-gradient(#c8d4e0,#2f4a6e)"><span class="tag" style="left:6px;bottom:6px"></span></div><p class="card-name">商品名</p><p class="card-price">価格</p></div>
    <div><div class="ph" role="img" aria-label="商品写真：ブラックウェア" style="background:linear-gradient(#ccc,#202020)"></div><p class="card-name">商品名</p><p class="card-price">価格</p></div>
    <div><div class="ph" role="img" aria-label="商品写真：プリントTシャツ" style="background:linear-gradient(#f0e8dc,#2a2a2a)"></div><p class="card-name">商品名</p><p class="card-price">価格</p></div>
    <div><div class="ph" role="img" aria-label="商品写真：白い布小物" style="background:linear-gradient(#fafafa,#d9c9b8)"><span class="tag" style="right:6px;top:6px"></span></div><p class="card-name">商品名</p><p class="card-price">価格</p></div>
  </div>
</section>
<div class="abs more-btn" style="left:348px;top:2960px">もっとみる</div>

<footer class="abs site-footer">
  <p class="footer-name">ハンドメイド shop ぽるみ</p>
  <ul class="footer-links">
    <li>送料について</li>
    <li>支払い方法について</li>
    <li>手数料</li>
    <li>納期</li>
    <li>キャンセルについて</li>
    <li>商品の在庫について</li>
  </ul>
</footer>

</body>
</html>
```